Business card design needed

My business is called The Driftwood Nook it is a small wine bar/cafe in the coastal town of Ocean Grove. We have great homestyle food, live acoustic music and a great range of beer wine and spirits. We are also available for private functions

Target Market(s)

Our market are people aged from 25 to 60

Industry/Entity Type

Town

Contact Information for Business Card

The Driftwood Nook
Shop 8 47 Marlow Parade
Seabrook Cove Victoria 3295

Harvey Pellman
03 59418276
0438172604
email driftwoodnookbay@mailbox-example.net

Requirements
Must have
• Black glossy card with gold writing

```html
<!DOCTYPE html>
<html lang="en">
<head>
<meta charset="utf-8">
<title>The Driftwood Nook – Business Card</title>
<link rel="stylesheet" href="https://fonts.googleapis.com/css2?family=Roboto+Condensed:wght@700&family=Ubuntu:wght@400;500&display=swap">
<style>
  :root {
    --page: #d9d6cf;
    --card-dark: #0d0d0d;
    --card-mid: #1c1c1c;
    --gold-deep: #a9782a;
    --gold: #d9aa4a;
    --gold-light: #f3d27a;
    --ink: #1a1408;
    --flourish: rgba(90, 90, 90, 0.16);
  }
  * { margin: 0; padding: 0; box-sizing: border-box; }
  html, body { width: 1200px; height: 790px; overflow: hidden; }
  body {
    background: var(--page);
    display: flex;
    align-items: center;
    justify-content: center;
  }
  .card {
    position: relative;
    width: 1000px;
    height: 612px;
    background: linear-gradient(150deg, var(--card-mid) 0%, var(--card-dark) 55%, var(--card-mid) 100%);
    box-shadow: 0 18px 40px rgba(0,0,0,0.35);
    overflow: hidden;
  }
  .flourish-pattern {
    position: absolute;
    inset: 0;
    background:
      radial-gradient(ellipse 420px 260px at 300px 360px, var(--flourish), transparent 70%),
      radial-gradient(ellipse 380px 240px at 820px 140px, var(--flourish), transparent 70%),
      radial-gradient(ellipse 360px 220px at 860px 520px, var(--flourish), transparent 70%);
  }
  .name-bar {
    position: absolute;
    left: 0;
    top: 80px;
    width: 400px;
    height: 78px;
    background: linear-gradient(90deg, var(--gold-deep) 0%, var(--gold) 45%, var(--gold-light) 80%, var(--gold) 100%);
    display: flex;
    align-items: center;
    padding-left: 44px;
  }
  .name-bar .person-name {
    font-family: "Roboto Condensed", sans-serif;
    font-weight: 700;
    font-size: 40px;
    color: var(--ink);
    letter-spacing: 0.5px;
  }
  .contact-list {
    position: absolute;
    left: 44px;
    top: 205px;
    list-style: none;
  }
  .contact-item {
    display: flex;
    align-items: center;
    height: 44px;
    margin-bottom: 34px;
    font-family: "Ubuntu", sans-serif;
    font-size: 27px;
    color: var(--gold-light);
    white-space: nowrap;
  }
  .contact-icon {
    width: 42px;
    height: 42px;
    margin-right: 20px;
    flex: none;
  }
  .brand {
    position: absolute;
    left: 580px;
    top: 130px;
    width: 380px;
    text-align: center;
    font-family: "Ubuntu", sans-serif;
    font-weight: 500;
    font-size: 48px;
    line-height: 1.15;
    letter-spacing: 3px;
    text-transform: uppercase;
    color: var(--gold);
  }
  .brand-dot {
    display: block;
    width: 22px;
    height: 22px;
    margin: 0 auto 22px;
    border-radius: 50%;
    background: var(--gold);
  }
</style>
</head>
<body>
  <main class="card">
    <div class="flourish-pattern" role="img" aria-label="Faint dark grey floral flourish pattern across the card background"></div>

    <div class="name-bar">
      <span class="person-name">Harvey Pellman</span>
    </div>

    <ul class="contact-list">
      <li class="contact-item">
        <svg class="contact-icon" viewBox="0 0 42 42" aria-hidden="true">
          <circle cx="21" cy="21" r="20" fill="var(--gold)"/>
          <rect x="15" y="9" width="12" height="24" rx="2" fill="var(--ink)"/>
          <rect x="17" y="12" width="8" height="15" fill="var(--gold-light)"/>
          <circle cx="21" cy="30" r="1.4" fill="var(--gold-light)"/>
        </svg>
        <span>0438172604</span>
      </li>
      <li class="contact-item">
        <svg class="contact-icon" viewBox="0 0 42 42" aria-hidden="true">
          <circle cx="21" cy="21" r="20" fill="var(--gold)"/>
          <rect x="11" y="17" width="20" height="14" rx="2" fill="var(--ink)"/>
          <path d="M10 16 q11 -8 22 0 v3 h-5 v-3 q-6 -3 -12 0 v3 h-5z" fill="var(--ink)"/>
          <circle cx="21" cy="24" r="3.2" fill="var(--gold-light)"/>
        </svg>
        <span>03 59418276</span>
      </li>
      <li class="contact-item">
        <svg class="contact-icon" viewBox="0 0 42 42" aria-hidden="true">
          <circle cx="21" cy="21" r="20" fill="var(--gold)"/>
          <rect x="10" y="13" width="22" height="16" rx="1.5" fill="var(--ink)"/>
          <path d="M11 14 l10 8 l10 -8" fill="none" stroke="var(--gold-light)" stroke-width="1.8"/>
        </svg>
        <span>driftwoodnookbay@mailbox-example.net</span>
      </li>
      <li class="contact-item">
        <svg class="contact-icon" viewBox="0 0 42 42" aria-hidden="true">
          <circle cx="21" cy="21" r="20" fill="var(--gold)"/>
          <path d="M9 22 L21 11 L33 22 h-4 v9 h-6 v-6 h-4 v6 h-6 v-9z" fill="var(--ink)"/>
        </svg>
        <span>8 47 Marlow Parade Seabrook Cove Victoria 3295</span>
      </li>
    </ul>

    <div class="brand">
      <span class="brand-dot" aria-hidden="true"></span>
      The Driftwood<br>Nook
    </div>
  </main>
</body>
</html>
```